Buch-/eBook-Cover für ein Fantasy Roman
Zielgruppe
Meine Zielgruppe sind Jugendliche und junge Erwachsene, aber auch für Ältere könnte mein Buch interessant sein.
Aufgabenstellung
Bei meinem Buch handelt es sich um einen Fantasy Roman. Es heißt 'Nachtfalter - Wahrheit braucht ihre Zeit' und der Autor ist Mara Oswaldtinger.
Das Buch handelt von einem Mädchen, welches eigentlich ein ganz normales Leben führt, aber dieses durch eine Pressekonferenz vom Präsidenten komplett durcheinander gerät. Denn viele Menschen sollen an einem Virus leiden. Die Menschen sollen sich aber keine Sorgen machen. Doch alles läuft durcheinander, da die infizierten Menschen einer nach dem anderen spurlos verschwinden.
Auf meinem Cover soll keine Figur zu sehen sein. Ich hätte gerne ein Zusammenspiel zwischen den Farben Blau und Grün. sie sollen harmonisch und fließend ineinander übergehen. Auch etwas Glitzer für etwas Geheimnisvolles darf auf dem Cover sein. Den Titel hätte ich gerne in der Mitte. Wo der Autorname stehen soll, bin ich offen.

```html
<!DOCTYPE html>
<html lang="de">
<head>
<meta charset="utf-8">
<title>Nachtfalter – Buchcover</title>
<link rel="stylesheet" href="https://fonts.googleapis.com/css2?family=Open+Sans:wght@400&family=Playfair+Display:wght@700&family=Satisfy&display=swap">
<style>
  :root {
    --backdrop: #e2e2e2;
    --deep-navy: #102a38;
    --ocean-teal: #14586a;
    --sea-green: #1e7a7a;
    --mist-green: #4f9a86;
    --gold-glow: #a9b06a;
    --ink-white: #ffffff;
  }
  * { margin: 0; padding: 0; box-sizing: border-box; }
  html, body {
    width: 1200px;
    height: 857px;
    overflow: hidden;
    background: var(--backdrop);
  }
  .book-cover {
    position: absolute;
    left: 342px;
    top: 44px;
    width: 516px;
    height: 769px;
    overflow: hidden;
    color: var(--ink-white);
    text-align: center;
  }
  .cover-artwork {
    position: absolute;
    inset: 0;
    background:
      radial-gradient(ellipse 45% 22% at 52% 2%, rgba(169,176,106,0.75), transparent 70%),
      radial-gradient(ellipse 60% 35% at 55% 18%, rgba(79,154,134,0.7), transparent 75%),
      radial-gradient(ellipse 70% 40% at 70% 45%, rgba(30,122,122,0.6), transparent 80%),
      radial-gradient(ellipse 60% 40% at 20% 70%, rgba(20,88,106,0.7), transparent 80%),
      linear-gradient(170deg, var(--sea-green) 0%, var(--ocean-teal) 45%, var(--deep-navy) 100%);
  }
  .author-name {
    position: absolute;
    top: 52px;
    left: 0;
    right: 0;
    font-family: "Open Sans", sans-serif;
    font-weight: 400;
    font-size: 23px;
    letter-spacing: 1.5px;
    text-transform: uppercase;
  }
  .book-title {
    position: absolute;
    top: 224px;
    left: 0;
    right: 0;
    font-family: "Playfair Display", serif;
    font-weight: 700;
    font-size: 44px;
    line-height: 1;
    text-transform: uppercase;
    letter-spacing: 0.5px;
  }
  .book-title .initial {
    font-size: 76px;
  }
  .book-subtitle {
    position: absolute;
    top: 338px;
    left: 0;
    right: 0;
    font-family: "Satisfy", cursive;
    font-size: 54px;
    line-height: 65px;
  }
  .book-subtitle span { display: block; }
</style>
</head>
<body>
  <main class="book-cover">
    <div class="cover-artwork" role="img" aria-label="Gemalter fließender Hintergrund in Blau- und Grüntönen mit feinen goldenen Linien und Glitzerpunkten"></div>
    <p class="author-name">Mara Oswaldtinger</p>
    <h1 class="book-title"><span class="initial">N</span>achtfalter</h1>
    <p class="book-subtitle">
      <span>Wahrheit</span>
      <span>braucht</span>
      <span>ihre</span>
      <span>Zeit</span>
    </p>
  </main>
</body>
</html>
```